Splash Page Design For Thailands "Whatever Suits Me" App

We are creating an app that will allow a tourist to request a variety of services on demand. Such as motorbike rentals, in room massage, pick up and laundry delivery service, maid cleaning service, etc.

We want to design a splash page that tourists will initially go to when they want to choose a service that we offer.

INSTRUCTIONS:
This page must speak to tourists in Phuket, Thailand. Should be Thailand Island theme.

GO 4 IT (logo)

CONTENT:

ALL YOU NEED WHILE TRAVELING IN PHUKET, THAILAND

CHOOSE A SERVICE BELOW TO GET STARTED

MOTORBIKE RENTALS
ACTIVITY AND TOUR PACKAGES (COMING SOON)
LAUNDRY PICK UP AND DELIVER SERVICE (COMING SOON)
MAID SERVICE (COMING SOON)
MASSAGE SERVICE TO YOUR ROOM (COMING SOON)
VISA SERVICE (COMING SOON)

Target Market(s)

TOURISTS IN PHUKET THAILAND

Industry/Entity Type

TOURISM

Number of Pages Required

1 page

Requirements
Must have
• We are creating an app that will allow a tourist to request a variety of services on demand. Such as motorbike rentals, in room massage, pick up and laundry delivery service, maid cleaning service, etc. We want to design a splash page that tourists will initially go to when they want to choose a service that we offer. INSTRUCTIONS: This page must speak to tourists in Phuket, Thailand. Should be Thailand Island theme. GO 4 IT (logo) CONTENT: ALL YOU NEED WHILE TRAVELING IN PHUKET, THAILAND CHOOSE A SERVICE BELOW TO GET STARTED MOTORBIKE RENTALS ACTIVITY AND TOUR PACKAGES (COMING SOON) LAUNDRY PICK UP AND DELIVER SERVICE (COMING SOON) MAID SERVICE (COMING SOON) MASSAGE SERVICE TO YOUR ROOM (COMING SOON) VISA SERVICE (COMING SOON)
Nice to have
Should not have

```html
<!DOCTYPE html>
<html lang="en">
<head>
<meta charset="utf-8">
<title>GO 4 IT — Whatever Suits Me in Phuket</title>
<link href="https://fonts.googleapis.com/css2?family=Poppins:wght@800&family=Merriweather:wght@300&family=Mulish:wght@400&display=swap" rel="stylesheet">
<style>
  :root {
    --orange: #e8641e;
    --sand: #f3d5a0;
    --sand-line: #e2c089;
    --ink: #3a2a1c;
    --white: #ffffff;
    --sky: #1f63b4;
    --sea: #4fb7a4;
    --slot: rgba(232,100,30,.18);
  }
  * { box-sizing: border-box; margin: 0; padding: 0; }
  html, body { width: 1200px; height: 1113px; overflow: hidden; }
  body { background: var(--sand); font-family: "Merriweather", serif; color: var(--ink); position: relative; }

  .hero-scene {
    position: absolute; left: 0; top: 0; width: 1200px; height: 752px;
    background: linear-gradient(180deg,
      #15468f 0%, var(--sky) 14%, #4d8fcf 30%, #5e7f4e 38%, #55734a 44%,
      #3f8f86 46%, var(--sea) 54%, #7ccbb1 62%, #bfe0c7 67%, #efd3a0 72%, var(--sand) 100%);
  }

  .brand {
    position: absolute; left: 34px; top: 34px; display: flex; align-items: center; gap: 10px;
    color: var(--white); font-family: "Poppins", sans-serif; font-weight: 800; font-size: 24px; line-height: 30px;
  }
  .brand-mark { width: 18px; height: 18px; border-radius: 50%; background: var(--white); }

  .lang-switch {
    position: absolute; left: 1047px; top: 25px; width: 69px; height: 24px;
    border: 2px solid var(--white); display: flex; align-items: center; gap: 4px; padding-left: 6px;
    color: var(--white); font-family: "Mulish", sans-serif; font-size: 10px;
  }
  .lang-swatch { width: 22px; height: 12px; background: #2a3f8f; }
  .menu-toggle { position: absolute; left: 1136px; top: 24px; }

  .hero-copy { position: absolute; left: 0; top: 500px; width: 1200px; text-align: center; color: var(--white); font-family: "Poppins", sans-serif; font-weight: 800; text-shadow: 0 2px 6px rgba(0,0,0,.35); }
  .hero-title { font-size: 34px; letter-spacing: -0.9px; line-height: 40px; }
  .hero-sub { position: absolute; left: 339px; top: 61px; width: 523px; border-top: 2px solid var(--white); border-bottom: 2px solid var(--white); height: 49px; line-height: 45px; font-size: 24.5px; letter-spacing: -0.6px; }

  .services { position: absolute; left: 0; top: 806px; width: 1200px; height: 218px; display: flex; border-bottom: 1px solid var(--sand-line); }
  .service { border-right: 1px solid var(--sand-line); display: flex; flex-direction: column; align-items: center; text-align: center; padding-top: 20px; }
  .service:last-child { border-right: none; }
  .service-icon { width: 68px; height: 68px; }
  .service-label { margin-top: 36px; font-size: 13.5px; line-height: 20px; text-transform: uppercase; font-weight: 300; }
  .service--first .service-label { margin-top: 34px; }
  .icon-slot { width: 64px; height: 64px; border-radius: 6px; background: var(--slot); margin: 2px; }

  .copyright { position: absolute; top: 1062px; width: 1200px; text-align: center; font-family: "Mulish", sans-serif; font-size: 11px; color: var(--ink); }
</style>
</head>
<body>
  <div class="hero-scene" role="img" aria-label="Photo of limestone sea stacks rising from turquoise water off a sandy Phuket beach under blue sky"></div>

  <header>
    <div class="brand"><span class="brand-mark"></span><span class="brand-name">GO 4 IT</span></div>
    <div class="lang-switch"><span class="lang-swatch"></span>EN ▾</div>
    <svg class="menu-toggle" width="29" height="24" viewBox="0 0 29 24">
      <rect x="0" y="0" width="29" height="5" rx="1" fill="#fff"/>
      <rect x="0" y="9" width="29" height="5" rx="1" fill="#fff"/>
      <rect x="0" y="18" width="29" height="5" rx="1" fill="#fff"/>
    </svg>
  </header>

  <section class="hero-copy">
    <h1 class="hero-title">ALL YOU NEED WHILE TRAVELING IN PHUKET, THAILAND</h1>
    <h2 class="hero-sub">CHOOSE A SERVICE BELOW TO GET STARTED</h2>
  </section>

  <nav class="services">
    <div class="service service--first" style="width:193px">
      <svg class="service-icon" viewBox="0 0 68 68" fill="none" stroke="#e8641e" stroke-width="3">
        <circle cx="14" cy="44" r="9"/><circle cx="54" cy="44" r="9"/>
        <path d="M14 44 L26 30 L42 30 L54 44 M30 30 L34 22 L46 22 M46 22 L52 30"/>
      </svg>
      <p class="service-label">Motorbike<br>Rentals</p>
    </div>
    <div class="service" style="width:190px">
      <div class="icon-slot" role="img" aria-label="Icon of a person paddling a kayak"></div>
      <p class="service-label">Activity and<br>tour packages<br>(coming soon)</p>
    </div>
    <div class="service" style="width:225px">
      <svg class="service-icon" viewBox="0 0 68 68" fill="none" stroke="#e8641e" stroke-width="3">
        <rect x="14" y="6" width="40" height="54"/><line x1="14" y1="16" x2="54" y2="16"/>
        <circle cx="34" cy="37" r="13"/><circle cx="34" cy="37" r="7"/>
      </svg>
      <p class="service-label">Laundry pick up<br>and deliver service<br>(coming soon)</p>
    </div>
    <div class="service" style="width:193px">
      <div class="icon-slot" role="img" aria-label="Icon of a housekeeper with a mop and bucket"></div>
      <p class="service-label">Maid service<br>(coming soon)</p>
    </div>
    <div class="service" style="width:201px">
      <div class="icon-slot" role="img" aria-label="Icon of a back with massage stones"></div>
      <p class="service-label">Massage service<br>to your room<br>(coming soon)</p>
    </div>
    <div class="service" style="width:198px">
      <svg class="service-icon" viewBox="0 0 68 68" fill="none" stroke="#e8641e" stroke-width="3">
        <rect x="14" y="6" width="40" height="56" rx="2"/>
        <circle cx="34" cy="28" r="10"/><line x1="24" y1="28" x2="44" y2="28"/>
        <line x1="24" y1="48" x2="44" y2="48"/>
      </svg>
      <p class="service-label">Visa service<br>(coming soon)</p>
    </div>
  </nav>

  <footer class="copyright">Copyright © 2021 All Rights Reserved</footer>
</body>
</html>
```